Flyer-Design für Rasseclub
sehr angenehme Zusammenarbeit - tolle Vorschläge - Anregungen werden prompt umgesetzt. Vielen Dank für den schönen Flyer. Vom Drucker habe ich auch noch ein Lob erhalten. "Nicht jeder Grafiker / Designer liefere solche gute Qualität ab"
Zielgruppe
Wir sind ein Rasseclub für die Zebu-Züchter in der Schweiz. Wir setzen uns für die Interessen und die Verbreitung der Zeburinder ein. Mit unserem Flyer versuchen wir interessierten Personen einen kurzen Überblick über die Rasse zu verschaffen.
Aufgabenstellung
Wir wünschen uns einen Flyer im A4 Format, welcher 1 oder 2x gefalzt ist. Vorne und hinten Beschriftet / Gestaltet.

```html
<!DOCTYPE html>
<html lang="de">
<head>
<meta charset="utf-8">
<title>Rasseclub Zebu Alpin – Flyer</title>
<link rel="stylesheet" href="https://fonts.googleapis.com/css2?family=Source+Sans+3:wght@400;600;700&display=swap">
<style>
:root{
  --olive:#5e6a3a;
  --olive-light:#7b8557;
  --red:#e21f26;
  --white:#ffffff;
  --stage:#dcdcdc;
  --ink:#1d1d1b;
  --grass-top:#9db36a;
  --grass-bottom:#5f7f33;
}
*{box-sizing:border-box;margin:0;padding:0}
html,body{width:1200px;height:3905px;overflow:hidden}
body{background:var(--stage);font-family:"Source Sans 3",Arial,sans-serif;color:var(--ink);position:relative}
.sheet{position:absolute;display:flex;box-shadow:0 4px 8px rgba(0,0,0,.25);background:var(--white)}
.sheet::after{content:"";position:absolute;left:0;right:0;bottom:0;height:15px;background:var(--red)}
.panel{width:319px;height:100%;position:relative;display:flex;flex-direction:column;overflow:hidden}
.panel--olive{background:var(--olive);color:var(--white)}
.photo{width:100%;background:linear-gradient(180deg,var(--grass-top),var(--grass-bottom))}
.photo--fog{background:linear-gradient(180deg,#c9cdc4,#8fa464 45%,#5c7c30)}
.photo--sky{background:linear-gradient(180deg,#9fb0c4,#c9b88f 40%,#a4a36a)}
.band{height:15px;background:var(--olive-light);flex:none}
.copy{padding:0 36px}
.copy h2{font-size:15px;font-weight:700;letter-spacing:.3px;text-transform:uppercase;padding-bottom:10px;border-bottom:1.5px solid var(--red);margin-bottom:18px;width:235px}
.copy p{font-size:11.3px;line-height:13.6px;margin-bottom:6px}
.panel--olive .copy h2{color:var(--white)}
.contact-box{position:absolute;left:32px;width:251px;height:153px;background:var(--white);color:var(--olive);font-size:11px;padding:16px 12px}
.brand{height:117px;background:var(--white);display:flex;align-items:center;justify-content:center;gap:8px;flex:none}
.brand__mark{width:12px;height:12px;background:var(--red)}
.brand__name{font-size:19px;font-weight:700;letter-spacing:1px;color:var(--ink)}
.cover-title{flex:1;background:var(--olive);color:var(--white);text-align:right;padding:38px 38px 0 0}
.cover-title .kicker{font-size:21px;font-weight:400}
.cover-title .name{font-size:26px;font-weight:700;letter-spacing:.5px}
.illustration{background:radial-gradient(ellipse at center,#a67c65 0,#c8a996 45%,#fff 72%)}
</style>
</head>
<body>

<!-- Front cover -->
<section class="sheet" style="left:438px;top:88px;width:321px;height:677px">
  <div class="panel" style="width:321px">
    <div class="brand"><span class="brand__mark"></span><span class="brand__name">ZEBU ALPIN</span></div>
    <div class="photo" style="height:393px" role="img" aria-label="Foto: dunkelbrauner Zebustier auf einer Weide"></div>
    <div class="band"></div>
    <div class="cover-title"><div class="kicker">Rasseclub</div><div class="name">ZEBU ALPIN</div></div>
  </div>
</section>

<!-- Outside spread -->
<section class="sheet" style="left:120px;top:845px;width:956px;height:678px">
  <div class="panel">
    <div class="photo" style="height:351px" role="img" aria-label="Foto: Gruppe heller und gefleckter Zebus auf der Weide"></div>
    <div class="band"></div>
    <div class="copy" style="padding-top:32px">
      <h2>Herkunft</h2>
      <p>Die Zebus (Bos indicus) gehören zu den Buckelrindern, die sich nicht nur vom Erbgut, sondern auch vom äusseren Erscheinungsbild her stark von den anderen Rinderrassen in Europa unterscheiden. Die Zebus stammen ursprünglich aus Sri Lanka und dem südlichen Kaukasus. Heute sind sie auf der ganzen Welt verbreitet. Die Zeburasse wird in 600 Rasseschläge unterteilt: vom kleinsten Zwergzebu bis zu den grössten Brahma oder Nelore. Das Wort Zebu wird vom tibetanischen Wort „zeu“ respektive. „zeba“ abgeleitet, welches übersetzt Buckel heisst.</p>
    </div>
  </div>
  <div class="panel panel--olive" style="width:322px">
    <div class="copy" style="padding-top:58px">
      <h2>Rasseclub</h2>
      <p>Bei «Herdenverband Mittelland» sind über 150 Muttertiere der Rasse Zwergzebu und Zebu registriert. Der «Rasseclub Zebu Alpin» gibt es seit dem Jahr 2015. Alle, die Zebus in der Schweiz halten, sind im Rasseclub herzlich willkommen. Die Tiere können, wie jedes andere Rind auch, bei «Herdenverband Mittelland» angemeldet werden. Selbstverständlich können auch die anerkannten Stiere im Herdebuch vom «Herdenverband Mittelland» aufgenommen werden und sind somit als Zuchtstiere anerkannt.</p>
    </div>
    <div class="contact-box" style="top:468px">Ihr Zebuhalter in der Nähe:</div>
  </div>
  <div class="panel" style="width:315px">
    <div class="brand" style="height:118px"><span class="brand__mark"></span><span class="brand__name">ZEBU ALPIN</span></div>
    <div class="photo" style="height:387px" role="img" aria-label="Foto: dunkelbrauner Zebustier auf einer Weide"></div>
    <div class="band"></div>
    <div class="cover-title" style="padding-top:36px"><div class="kicker">Rasseclub</div><div class="name">ZEBU ALPIN</div></div>
  </div>
</section>

<!-- Inside spread -->
<section class="sheet" style="left:120px;top:1586px;width:956px;height:678px">
  <div class="panel">
    <div class="photo" style="height:262px" role="img" aria-label="Foto: weisser Zebu mit braunen Flecken auf der Wiese"></div>
    <div class="band"></div>
    <div class="copy" style="padding-top:58px">
      <h2 style="width:250px">Merkmale und Eigenschaften</h2>
      <p>Der Buckel ist das auffälligste, äussere Merkmal der Zeburinder. Das ausgesprochen marmorierte Buckelfleisch ist eine Delikatesse. Das übrige Muskelfleisch ist sehr fettarm, mit einem leichten Wildgeschmack, feinfaserig und enthält die gesunden Omega-3-Fettsäuren.</p>
      <p>Zum typischen Erscheinungsbild der Zebus gehören neben dem Buckel die Hörner, eine starke Wamme, ein abgezogenes und stark abgedachtes Becken, feine Extremitäten und eine schmale Stirn, die dem Kopf eine längliche Form verleiht.</p>
      <p>Die Grösse der Tiere kann stark variieren. Die Kühe sind deutlich kleiner als die Stiere. Zebus kommen in allen Farben und Farbkombinationen vor. Auch die Hörner sind nicht immer klassisch nach oben gerichtet.</p>
    </div>
  </div>
  <div class="panel" style="width:322px">
    <div class="copy" style="height:372px;padding-top:58px">
      <p>Zebus sind sehr robust und gehören zu den extensiven Rinderrassen. Die Klauenpflege kann auf ein Minimum beschränkt werden. Die Tiere sind betreffend Futter sehr genügsam. Ihnen reicht im Sommer Gras und im Winter Heu. Auf Kraftfutter und andere Zusätze, mit Ausnahme von Salz, kann verzichtet werden. Die Abkalbung ist meist leicht und geschieht ohne menschliche Hilfe. Die Mutterkühe haben einen guten Schutzinstinkt für ihre Kälber.</p>
      <p>Während die meisten europäischen Rinderrassen unter der Sommerhitze leiden, fühlen sich Zebus bei Temperaturen um 30 Grad noch wohl. Ihr schütteres Fell und die dicke Aussenhaut schützen sie vor der Hitze. In den letzten Jahren wurde beobachtet, dass Zebusperma auch bei Temperaturen über 38°C noch befruchtungsfähig bleibt. Kalte Temperaturen sind sie sich von ihrer Heimat auch gewohnt.</p>
    </div>
    <div class="band"></div>
    <div class="photo photo--fog" style="height:276px" role="img" aria-label="Foto: Zebuherde beim Fressen an der Heuraufe im Nebel"></div>
  </div>
  <div class="panel" style="width:315px">
    <div class="photo photo--sky" style="height:224px" role="img" aria-label="Foto: heller Zebu im Porträt vor Landschaft"></div>
    <div class="band"></div>
    <div class="copy" style="padding-top:40px">
      <h2>Einsatz</h2>
      <p>Durch ihr leichtes Gewicht verursachen Zebus kaum Trittschäden, wodurch sie fast überall einsetzbar sind. Sie können auch gut zur allgemeinen Landschaftspflege eingesetzt werden.</p>
    </div>
    <div class="illustration" style="margin:14px auto 0;width:200px;height:244px" role="img" aria-label="Illustration: stehender Zebustier in Braun"></div>
  </div>
</section>

<!-- Inside panels, flat -->
<section class="sheet" style="left:276px;top:2384px;width:638px;height:672px">
  <div class="panel">
    <div class="photo" style="height:262px" role="img" aria-label="Foto: weisser Zebu mit braunen Flecken auf der Wiese"></div>
    <div class="band"></div>
    <div class="copy" style="padding-top:38px">
      <h2 style="width:250px">Merkmale und Eigenschaften</h2>
      <p>Der Buckel ist das auffälligste, äussere Merkmal der Zeburinder. Das ausgesprochen marmorierte Buckelfleisch ist eine Delikatesse. Das übrige Muskelfleisch ist sehr fettarm, mit einem leichten Wildgeschmack, feinfaserig und enthält die gesunden Omega-3-Fettsäuren.</p>
      <p>Zum typischen Erscheinungsbild der Zebus gehören neben dem Buckel die Hörner, eine starke Wamme, ein abgezogenes und stark abgedachtes Becken, feine Extremitäten und eine schmale Stirn, die dem Kopf eine längliche Form verleiht.</p>
      <p>Die Grösse der Tiere kann stark variieren. Die Kühe sind deutlich kleiner als die Stiere. Zebus kommen in allen Farben und Farbkombinationen vor. Auch die Hörner sind nicht immer klassisch nach oben gerichtet.</p>
    </div>
  </div>
  <div class="panel">
    <div class="photo" style="height:351px" role="img" aria-label="Foto: Gruppe heller und gefleckter Zebus auf der Weide"></div>
    <div class="band"></div>
    <div class="copy" style="padding-top:32px">
      <h2>Herkunft</h2>
      <p>Die Zebus (Bos indicus) gehören zu den Buckelrindern, die sich nicht nur vom Erbgut, sondern auch vom äusseren Erscheinungsbild her stark von den anderen Rinderrassen in Europa unterscheiden. Die Zebus stammen ursprünglich aus Sri Lanka und dem südlichen Kaukasus. Heute sind sie auf der ganzen Welt verbreitet. Die Zeburasse wird in 600 Rasseschläge unterteilt: vom kleinsten Zwergzebu bis zu den grössten Brahma oder Nelore. Das Wort Zebu wird vom tibetanischen Wort „zeu“ respektive „zeba“ abgeleitet, welches übersetzt Buckel heisst.</p>
    </div>
  </div>
</section>

<!-- Back panel -->
<section class="sheet" style="left:438px;top:3116px;width:321px;height:676px">
  <div class="panel panel--olive" style="width:321px">
    <div class="copy" style="padding-top:60px">
      <h2>Rasseclub</h2>
      <p>Bei «Herdenverband Mittelland» sind über 150 Muttertiere der Rasse Zwergzebu und Zebu registriert. Der «Rasseclub Zebu Alpin» gibt es seit dem Jahr 2015. Alle, die Zebus in der Schweiz halten, sind im Rasseclub herzlich willkommen. Die Tiere können, wie jedes andere Rind auch, bei «Herdenverband Mittelland» angemeldet werden. Selbstverständlich können auch die anerkannten Stiere im Herdebuch vom «Herdenverband Mittelland» aufgenommen werden und sind somit als Zuchtstiere anerkannt.</p>
    </div>
    <div class="contact-box" style="top:470px">Ihr Zebuhalter in der Nähe:</div>
  </div>
</section>

</body>
</html>
```